" Nome da empresa: Recanto Vivale CLINICA DE NUTRIÇAO SOMOS NUTRICIONISTAS E DESEJAMOS PROPORCIONAR AOS NOSSOS PACIENTES UM TRATAMENTO INDIVIDUALIZADO. FAREMOS ATENDIMENTOS NUTRICIONAIS A FIM DE LEVAR QUALIDADE DE VIDA E PREVENÇAO de doenças, focando na educaçao nutricional "

```html
<!DOCTYPE html>
<html lang="pt-BR">
<head>
<meta charset="UTF-8">
<title>Recanto Vivale — Pasta</title>
<link rel="stylesheet" href="https://fonts.googleapis.com/css2?family=Quicksand:wght@400;500;600&display=swap">
<style>
  :root {
    --canvas: #ece8e2;
    --forest: #1d5650;
    --gold: #d9a23a;
    --paper: #ffffff;
    --ink-soft: #2c6a5f;
    --line-light: #e6eeec;
  }
  * { margin: 0; padding: 0; box-sizing: border-box; }
  html, body {
    width: 1200px; height: 1200px; overflow: hidden;
    background: var(--canvas);
    font-family: "Quicksand", sans-serif;
  }
  .folder {
    position: absolute;
    left: 150px; top: 130px;
    width: 900px; height: 940px;
    display: flex;
  }
  .panel { position: relative; width: 450px; height: 100%; }
  .panel--cover {
    background: var(--forest);
    clip-path: polygon(0 0, 100% 0, 100% 85%, 92% 100%, 0 100%);
  }
  .panel--inside {
    background: var(--paper);
    box-shadow: 0 0 0 1px #ddd inset;
  }
  .cover-emblem {
    position: absolute; left: 50%; top: 276px;
    transform: translateX(-50%);
    width: 228px; height: 228px;
    border: 4px solid var(--gold);
    border-radius: 50%;
    display: flex; align-items: center; justify-content: center;
  }
  .cover-emblem__name {
    color: var(--gold);
    font-weight: 500;
    font-size: 27px;
    text-align: center;
    line-height: 1.2;
  }
  .cover-signature {
    position: absolute; left: 0; right: 0; top: 676px;
    text-align: center;
    color: var(--paper);
    font-weight: 500;
    font-size: 15px;
  }
  .cover-contact {
    position: absolute; left: 0; right: 0; top: 712px;
    text-align: center;
    color: var(--line-light);
    font-size: 8.5px;
    letter-spacing: 0.1px;
  }
  .brand {
    position: absolute; left: 0; right: 0; top: 296px;
    display: flex; flex-direction: column; align-items: center;
  }
  .brand__dot {
    width: 86px; height: 86px;
    border: 3px solid var(--gold);
    border-radius: 50%;
  }
  .brand__name {
    margin-top: 12px;
    color: var(--forest);
    font-weight: 500;
    font-size: 48px;
    letter-spacing: 0.5px;
  }
  .brand__tagline {
    margin-top: 6px;
    color: var(--ink-soft);
    font-size: 13px;
    letter-spacing: 0.3px;
  }
</style>
</head>
<body>
  <main class="folder">
    <section class="panel panel--cover">
      <div class="cover-emblem">
        <span class="cover-emblem__name">Recanto<br>Vivale</span>
      </div>
      <p class="cover-signature">Recanto Vivale</p>
      <p class="cover-contact">Telefone (00) 0000-0000 | contato@recantovivale.com.br | Rua das Palmeiras, 120 · Centro · Cidade Nova</p>
    </section>
    <section class="panel panel--inside">
      <div class="brand">
        <span class="brand__dot"></span>
        <h1 class="brand__name">Recanto Vivale</h1>
        <p class="brand__tagline">Saúde · Ciência · Educação Nutricional</p>
      </div>
    </section>
  </main>
</body>
</html>
```